CREATE A KILLER WEBSITE DESIGN

We are a firearms training company that trains CIVILIANS (no police or military pictures - thank you!) to defend themselves and are looking for a killer design that's clean, easy to navigate and modern! We want the newest trends applied to this sight like a scrollable site so you can scroll down and see all the features. We are okay with tweaking the HTML but need the artistic design to look good. I'll provide a link to our current site along with a sight we really like so you can get an idea!

I'm supplying a PowerPoint Design we are going with from another designer so you can match the style to the new site.

PAGES: (Please use information from our current site. We like the information but just want a more polished look similar to the NWDLA site below but in our colors.)
Home - Long Form Scrolling Site. Top fold will be a video with a play button.
Falcon Institute - Seven Level Training Program Info Page That Will Contain A Video.
Contact Us - This will be a page that DOES NOT CONTAIN AN EMAIL ADDRESS. Just a contact us form
Meet The Trainer: Morgan Pellbrook

Our site:
https://www.brisklanewardens.biz

Sights We Like:
https://www.nwdefenseleague.example.com
https://quorvel.example.com
https://brantforgeworks.example.com
https://www.pelnrigear.example.com

Target Market(s)

Men and women ages 21 to 100 years old

Industry/Entity Type

Self Defense

Number of Pages Required

5+ page

Font styles to use
Sans Serif

Colors
f26267

Requirements
Must have
• Clean and engaging. Use of colors that match our logo.
Should not have
• Poor design quality

```html
<!DOCTYPE html>
<html lang="en">
<head>
<meta charset="utf-8">
<title>Brisklane Wardens – Concealed Carry Training</title>
<link href="https://fonts.googleapis.com/css2?family=Russo+One&family=Montserrat:ital,wght@0,400;0,500;0,600;0,700;1,400&display=swap" rel="stylesheet">
<style>
:root{
  --red:#e41d1d;
  --dark:#333333;
  --darker:#262626;
  --ink:#222222;
  --grey:#555555;
  --light:#f4f4f4;
  --white:#ffffff;
  --line:#cfcfcf;
}
*{box-sizing:border-box;margin:0;padding:0}
html,body{width:1200px;height:4497px;overflow:hidden}
body{position:relative;background:var(--white);font-family:"Montserrat",sans-serif;color:var(--ink)}
.abs{position:absolute}
.display{font-family:"Russo One",sans-serif;text-transform:uppercase;letter-spacing:2px}
svg.band{position:absolute;left:0;display:block}

/* top bar + nav */
.topbar{top:0;left:0;width:1200px;height:48px;background:var(--dark);color:var(--white);font-size:12px;font-weight:600}
.topbar .links{position:absolute;left:96px;top:16px;display:flex;gap:30px}
.topbar .acct{position:absolute;right:96px;top:16px;display:flex;gap:26px}
.navbar{top:48px;left:0;width:1200px;height:60px;background:var(--white)}
.brand{position:absolute;left:90px;top:20px;font-family:"Russo One",sans-serif;font-size:17px;color:var(--red);display:flex;align-items:center;gap:6px}
.brand .dot{width:12px;height:12px;border-radius:50%;background:var(--red)}
.menu{position:absolute;left:262px;top:22px;display:flex;gap:22px;font-weight:600;font-size:15px;color:#333}
.urgent{position:absolute;left:906px;top:14px;width:202px;height:31px;border-radius:16px;background:var(--red);color:var(--white);font-size:11px;font-weight:600;display:flex;align-items:center;justify-content:center}
.search{position:absolute;left:864px;top:20px}

/* hero */
.hero-photo{top:108px;left:0;width:1200px;height:565px;background:linear-gradient(180deg,#5a5a58 0%,#4a4a48 55%,#3b3b3a 100%)}
.hero-title{top:205px;left:0;width:1200px;text-align:center;color:var(--white);font-size:33px;line-height:38px}
.hero-sub{top:388px;left:0;width:1200px;text-align:center;color:var(--white);font-size:22px;line-height:25px}
.pill{position:absolute;height:36px;border-radius:18px;font-size:13px;font-weight:600;display:flex;align-items:center;justify-content:center}
.pill.ghost{background:var(--white);color:var(--red)}
.pill.solid{background:var(--red);color:var(--white)}
.play{top:562px;left:510px;width:180px;height:47px;border:2px solid #cfcfcf;background:rgba(30,30,30,.55);color:var(--white);font-weight:700;font-size:16px;display:flex;align-items:center;justify-content:center;gap:12px}

/* quote */
.quote-box{top:803px;left:325px;width:548px;height:163px;border:4px solid #5a5a5a;color:var(--white);font-size:21px;line-height:26px;text-align:center;padding-top:34px}
.target{position:absolute}

/* about */
.portrait{top:1206px;left:92px;width:472px;height:472px;border-radius:50%;border:3px solid var(--red);background:radial-gradient(circle at 50% 40%,#d8d8d8 0%,#9c9c9c 60%,#6a6a6a 100%)}
.about-kicker{top:1160px;left:679px;font-size:15px;color:#444}
.about-name{top:1182px;left:679px;font-size:22px;color:var(--ink)}
.about-name span{color:var(--red)}
.about-text{top:1232px;left:606px;width:500px;font-size:13.4px;line-height:21px;color:#444}
.about-text p+p{margin-top:21px}

/* seen on */
.seen-label{top:1835px;left:0;width:1200px;text-align:center;color:var(--white);font-size:15px}
.seen-logos{top:1888px;left:330px;width:540px;display:flex;justify-content:space-between;align-items:center;color:var(--white);font-weight:700;font-size:17px}

/* levels */
.levels-title{top:2060px;left:178px;color:var(--white);font-size:34px;line-height:38px}
.levels-text{top:2214px;left:178px;width:580px;color:var(--white);font-size:13.6px;line-height:21px}
.levels-text p+p{margin-top:21px}
.level{position:absolute;display:flex;align-items:center;gap:14px;color:var(--white);font-size:13.6px;line-height:21px;font-weight:500}
.level .num{font-family:"Russo One",sans-serif;font-size:52px;color:#5b5b5b;line-height:1}
.helmet-space{top:2050px;left:832px;width:200px;height:290px}

/* video card */
.card-video{top:2846px;left:159px;width:494px;height:323px;border-radius:30px 0 0 30px;background:linear-gradient(135deg,#d9d9d9 0%,#a9a9a9 60%,#8a8a8a 100%)}
.card-info{top:2846px;left:620px;width:447px;height:323px;border-radius:0 30px 30px 0;background:var(--dark)}
.card-brand{top:2930px;left:680px;color:var(--white);font-family:"Russo One",sans-serif;font-size:15px;display:flex;align-items:center;gap:6px}
.card-title{top:2882px;left:835px;color:var(--white);font-size:25px;line-height:29px}
.card-text{top:3007px;left:835px;width:210px;color:var(--white);font-size:13.6px;line-height:21px}

/* stories */
.stories-title{top:3432px;left:0;width:1200px;text-align:center;font-size:31px;color:var(--ink)}
.story{position:absolute;width:270px;font-size:13.6px;line-height:21px;color:#555}
.story q{font-style:italic;quotes:none;display:block;height:120px}
.story .rule{width:32px;height:2px;background:var(--red);margin:0 0 8px}
.story .who{font-family:"Russo One",sans-serif;font-size:15px;color:var(--ink);letter-spacing:1px}
.story .when{font-size:12px;color:#777}

/* contact */
.contact-card{top:3916px;left:168px;width:368px;height:374px;background:var(--white);padding:46px 42px 0}
.contact-card .k{color:var(--red);font-size:18px}
.contact-card .n{color:var(--ink);font-size:20px;margin-top:6px}
.contact-card .cred{font-size:11px;line-height:19px;color:#555;margin-top:14px}
.crow{display:flex;gap:14px;font-size:13px;line-height:21px;color:#555;margin-top:10px}
.crow b{font-weight:700}
.field{position:absolute;left:583px;width:447px;background:var(--white);font-size:13px;color:#777;padding:14px 0 0 40px;font-weight:500}
.field sup{color:var(--red)}
.submit{top:4332px;left:842px;width:188px;height:54px;background:var(--red);color:var(--white);font-weight:700;font-size:16px;display:flex;align-items:center;justify-content:center}
.footbar{top:4435px;left:0;width:1200px;height:62px;background:var(--darker);color:var(--white);font-size:12px}
.social{position:absolute;top:22px;width:20px;height:20px;border-radius:50%;background:var(--red)}
.copy{position:absolute;right:92px;top:24px}
</style>
</head>
<body>

<header class="abs topbar">
  <nav class="links"><span>Home</span><span>Upcoming Classes</span><span>Shop</span><span>Videos</span></nav>
  <div class="acct"><span>Log In</span><span>Cart 0</span></div>
</header>

<div class="abs navbar">
  <div class="brand"><span class="dot"></span>BRISKLANE</div>
  <nav class="menu"><span>Falcon Institute</span><span>Testimonials</span><span>About</span><span>Lost Certificate</span></nav>
  <svg class="search" width="20" height="20" viewBox="0 0 20 20"><circle cx="8" cy="8" r="6" fill="none" stroke="#555" stroke-width="2"/><line x1="12.5" y1="12.5" x2="18" y2="18" stroke="#555" stroke-width="2"/></svg>
  <div class="urgent">I NEED IMMEDIATE SERVICE</div>
</div>

<section>
  <div class="abs hero-photo" role="img" aria-label="Photo of a civilian shooting range with two pistols shown on either side"></div>
  <h1 class="abs hero-title display">Don't be fooled.<br>All concealed weapons<br>classes are not created<br>equal</h1>
  <p class="abs hero-sub">There is a difference<br>Hands on training<br>Real world scenarios</p>
  <div class="pill ghost" style="top:498px;left:409px;width:188px">FALCON INSTITUTE</div>
  <div class="pill solid" style="top:498px;left:611px;width:180px">GET TICKETS NOW</div>
  <div class="abs play">Play Video
    <svg width="26" height="20" viewBox="0 0 26 20"><rect x="1" y="1" width="24" height="18" fill="none" stroke="#fff" stroke-width="2"/><path d="M10 5 L17 10 L10 15 Z" fill="#fff"/></svg>
  </div>
</section>

<svg class="band" style="top:640px" width="1200" height="470" viewBox="0 0 1200 470">
  <polygon points="0,30 1200,8 1200,22 0,44" fill="var(--red)"/>
  <polygon points="0,44 1200,22 1200,359 600,463 0,359" fill="var(--dark)"/>
  <polygon points="0,44 1200,22 1200,6 600,40 0,30" fill="var(--red)" opacity="0"/>
</svg>

<svg class="target" style="top:785px;left:580px" width="40" height="40" viewBox="0 0 40 40"><circle cx="20" cy="20" r="18" fill="none" stroke="#e41d1d" stroke-width="3"/><circle cx="20" cy="20" r="11" fill="none" stroke="#e41d1d" stroke-width="3"/><circle cx="20" cy="20" r="4" fill="#e41d1d"/></svg>
<blockquote class="abs quote-box display">"Your life may depend on what<br>you learn in your concealed<br>carry training - don't settle<br>for a gun shop class!"</blockquote>

<section>
  <div class="abs portrait" role="img" aria-label="Black and white portrait of instructor Morgan Pellbrook"></div>
  <svg class="target" style="top:1158px;left:606px" width="48" height="48" viewBox="0 0 40 40"><circle cx="20" cy="20" r="18" fill="none" stroke="#e41d1d" stroke-width="3"/><circle cx="20" cy="20" r="11" fill="none" stroke="#e41d1d" stroke-width="3"/><circle cx="20" cy="20" r="4" fill="#e41d1d"/></svg>
  <p class="abs about-kicker">ABOUT THE INSTRUCTOR</p>
  <h2 class="abs about-name display"><span>Morgan</span> Pellbrook</h2>
  <div class="abs about-text">
    <p>Morgan Pellbrook is a 3rd generation Jacksonville native and delighted to be a part of this great community. He is a true security expert with 25 years of experience in the security industry. He has appeared on Harbor Nine, Meridian TV, Northstar &amp; Crestline news outlets. He has been Featured in numerous publications and has trained thousands to protect themselves and their homes from thugs and thieves. He is certified by both the NFSA &amp; the NWDLA as a firearms instructor. He is also an NFSA Range Safety Officer and Defensive Pistol Instructor. He often says: "My students are like family so I take their security personal. I want them to feel confident that they can protect themselves and their families!"</p>
    <p>Brisklane Wardens is a radically different concealed carry class focusing on the TRUTH about how "Real Attacks" take place. The Concealed Carry Class goes over way more than just the boring, lecture-style, gun shop curriculum into real strategies, tactics and training suggestions to help you prepare! You have to experience it to believe it! We also offer The Falcon Institute for those who are looking for a Fully Immersive, Reality Based training environment that prepares you to defend against the worst threats you may face! In The Institute, we utilize high tech, military/law enforcement grade simulators to take training to a level never before seen in the world of concealed carry.</p>
  </div>
</section>

<svg class="band" style="top:1764px" width="1200" height="1020" viewBox="0 0 1200 1020">
  <polygon points="0,101 600,0 1200,101 1200,166 600,253 0,166" fill="var(--red)"/>
  <polygon points="0,166 600,253 1200,166 1200,908 600,1016 0,908" fill="var(--dark)"/>
</svg>
<p class="abs seen-label display">• • • &nbsp;As seen on&nbsp; • • •</p>
<div class="abs seen-logos"><span>Harbor Nine</span><span>Crestline</span><span style="font-size:22px">Meridian TV</span><span>Northstar</span></div>

<section>
  <svg class="target" style="top:2067px;left:92px" width="48" height="48" viewBox="0 0 40 40"><circle cx="20" cy="20" r="18" fill="none" stroke="#e41d1d" stroke-width="3"/><circle cx="20" cy="20" r="11" fill="none" stroke="#e41d1d" stroke-width="3"/><circle cx="20" cy="20" r="4" fill="#e41d1d"/></svg>
  <h2 class="abs levels-title display">Our 7 levels of<br>training take you<br>from zero to hero</h2>
  <div class="abs levels-text">
    <p>Wanna hear something funny? Guess what the average person asks about a concealed weapons class? "How much is it and how long is it?" Can you believe it? We are talking about preparing you for life and death situations and the main concern is "How Fast" and "How Cheap?" WOW!</p>
    <p>Why do most people settle for a cheap &amp; quick concealed carry class? It's a fair question! Could you imagine a military soldier trained by a 2-hour class? How effective would they be in the heat of battle? If you want to be ready to SURVIVE an attack, YOU NEED MORE than a basic, run of the mill class! That's why we created a PROPRIETARY 7 LEVEL TRAINING SYSTEM to take you all the way to the peak of readiness!</p>
  </div>
  <div class="pill solid" style="top:2369px;left:869px;width:149px">Learn more</div>
  <div class="level" style="top:2530px;left:178px"><span class="num">1</span>CONCEALED<br>CARRY CLASS</div>
  <div class="level" style="top:2530px;left:384px"><span class="num">2</span>DYNAMIC DEFENSIVE<br>SHOOTING</div>
  <div class="level" style="top:2530px;left:660px"><span class="num">3</span>FINE TUNING YOUR<br>TECHNIQUE</div>
  <div class="level" style="top:2530px;left:938px"><span class="num">4</span>VIRTUAL<br>THREAT-LAB</div>
  <div class="level" style="top:2620px;left:178px"><span class="num">5</span>TACTICAL SKILLS<br>&amp; DRILLS</div>
  <div class="level" style="top:2620px;left:384px"><span class="num">6</span>CLOSE QUARTERS<br>DEFENSE</div>
  <div class="level" style="top:2620px;left:660px"><span class="num">7</span>LIVE SCENARIO<br>THREAT-LAB</div>
</section>

<div class="abs" style="top:2780px;left:0;width:1200px;height:440px;background:var(--light);z-index:-1"></div>
<section>
  <div class="abs card-info"></div>
  <div class="abs card-video" role="img" aria-label="Video still of a hand holding a silver pistol"></div>
  <svg class="abs" style="top:2980px;left:367px" width="76" height="76" viewBox="0 0 76 76"><circle cx="38" cy="38" r="36" fill="var(--red)"/><path d="M31 26 L50 38 L31 50 Z" fill="#fff"/></svg>
  <div class="abs card-brand"><span class="dot" style="width:12px;height:12px;border-radius:50%;background:var(--red)"></span>BRISKLANE</div>
  <h2 class="abs card-title display">Join the<br>Falcon<br>Institute</h2>
  <p class="abs card-text">A FULLY IMMERSIVE training SYSTEM PREPARING YOU TO PREVAIL</p>
  <div class="pill solid" style="top:3091px;left:835px;width:148px">Learn more</div>
</section>

<section>
  <svg class="target" style="top:3366px;left:576px" width="48" height="48" viewBox="0 0 40 40"><circle cx="20" cy="20" r="18" fill="none" stroke="#e41d1d" stroke-width="3"/><circle cx="20" cy="20" r="11" fill="none" stroke="#e41d1d" stroke-width="3"/><circle cx="20" cy="20" r="4" fill="#e41d1d"/></svg>
  <h2 class="abs stories-title display">Success stories</h2>
  <div class="story" style="top:3522px;left:147px"><q>"I had never held a gun when I took the Brisklane Wardens class and I'm hooked! I'm going all the way to level 7! Thank you Brisklane Wardens!"</q><div class="rule"></div><div class="who">RENATA K.</div><div class="when">October 14, 2017</div></div>
  <div class="story" style="top:3522px;left:412px"><q>"I was mugged here in Jacksonville and lived in fear ever since. It stole my happiness and I became scared to go out. I'm a Level 4 student and I feel sorry for the next thug that tries me!"</q><div class="rule"></div><div class="who">DELPHINE R.</div><div class="when">December 9, 2017</div></div>
  <div class="story" style="top:3522px;left:705px;width:350px"><q>"I've been shooting for years and already had my concealed weapons license. My first class was a gun shop class and a waste of money. Morgan took the time to show me how to properly grip my gun and my shooting dramatically improved!"</q><div class="rule"></div><div class="who">OWEN T.</div><div class="when">March 3 2018</div></div>
</section>

<svg class="band" style="top:3740px" width="1200" height="700" viewBox="0 0 1200 700">
  <polygon points="0,101 600,0 1200,101 1200,700 0,700" fill="var(--dark)"/>
  <polygon points="0,88 600,-6 600,4 0,112" fill="var(--red)"/>
</svg>

<section>
  <div class="abs contact-card">
    <p class="k display">Meet the trainer:</p>
    <p class="n display">Morgan Pellbrook</p>
    <p class="cred">NFSA FIREARMS INSTRUCTOR, NWDLA INSTRUCTOR &amp; TRAINING COUNSELLOR, NEWS CORRESPONDENT, AND SECURITY EXPERT</p>
    <div class="crow"><svg width="14" height="20" viewBox="0 0 14 20"><path d="M7 0 C3 0 0 3 0 7 C0 12 7 20 7 20 C7 20 14 12 14 7 C14 3 11 0 7 0 Z" fill="var(--red)"/><circle cx="7" cy="7" r="2.5" fill="#fff"/></svg><span>P.O. Box 4410<br>Coral Bend, FL 32990</span></div>
    <div class="crow"><svg width="14" height="16" viewBox="0 0 14 16"><path d="M3 0 L6 4 L4 6 C5 9 7 11 10 12 L12 10 L14 13 L11 16 C5 15 0 9 0 3 Z" fill="var(--red)"/></svg><b>LOCAL: 555-014-2277<br>TOLL-FREE: 555-019-4630</b></div>
    <div class="crow"><svg width="14" height="12" viewBox="0 0 14 12"><rect width="14" height="12" fill="var(--red)"/><path d="M0 0 L7 6 L14 0" fill="none" stroke="#fff" stroke-width="1.5"/></svg><span>hello@brisklanewardens.example.com</span></div>
  </div>
  <div class="field" style="top:3920px;height:56px">Name <sup>*</sup></div>
  <div class="field" style="top:3998px;height:56px">Email <sup>*</sup></div>
  <div class="field" style="top:4077px;height:56px">Phone</div>
  <div class="field" style="top:4155px;height:135px">Message</div>
  <div class="abs submit">Submit</div>
</section>

<footer class="abs footbar">
  <span class="social" style="left:92px"></span>
  <span class="social" style="left:126px"></span>
  <span class="social" style="left:160px"></span>
  <p class="copy">Copyright Brisklane Wardens 2021 - All Rights Reserved</p>
</footer>

</body>
</html>
```